Tozvar new design for business cards we want to change our existing design. Logo must remain the same

Hello we are the company TozVar and offer various services regarding transportation and disposal. In addition to our main acquisition of van rental, we also offer disposal and express transportation, so we need new business card designs for our business. Our elders have their time and do not like it anymore. We want to change our existing design. Logo must remain the same as well as the color blue, whether dark or light Does not play a big role in the best medium blue. Logo must be present on the front side. As well as telephone, email, web and location. Big enough but not too big. Back can be redesigned Logo as well as name TozVar must be present. Important is the text: Van rental Disposal and clearing express transportation. Without bail in red should be noted somewhere. it should be modern but not too playful. rather serious but no beating company Thank you very much

Target Market(s)

Private customers as well as companies we want to change our existing design. Logo must remain the same as well as the color blue, whether dark or light Does not play a big role in the best medium blue. Logo must be present on the front side. As well as telephone, email, web and location. Big enough but not too big. Back can be redesigned Logo as well as name TozVar must be present. Important is the text: Van rental Disposal and clearing express transportation. Without bail in red should be noted somewhere. it should be modern but not too playful. rather serious but no beating company Thank you very much

Industry/Entity Type

Car Rental

Contact Information for Business Card

we want to change our existing design. Logo must remain the same as well as the color blue, whether dark or light Does not play a big role in the best medium blue.
Logo must be present on the front side.
As well as telephone, email, web and location. Big enough but not too big.
Back can be redesigned Logo as well as name TozVar must be present.
Important is the text:
Van rental
Disposal and clearing
Express transportation.
Without bail in red should be noted somewhere.
it should be modern but not too playful. rather serious but no beating company
Thank you very much

Font styles to use
Sans Serif

Colors
33a6d7
ec1f27
0692cd
3277b5

Requirements
Must have
• logo and name TozVar as described in the above text must have it. we want to change our existing design. Logo must remain the same as well as the color blue, whether dark or light Does not play a big role in the best medium blue. Logo must be present on the front side. As well as telephone, email, web and location. Big enough but not too big. Back can be redesigned Logo as well as name TozVar must be present. Important is the text: Van rental Disposal and clearing express transportation. Without bail in red should be noted somewhere. it should be modern but not too playful. rather serious but no beating company Thank you very much
Nice to have
• see description we want to change our existing design. Logo must remain the same as well as the color blue, whether dark or light Does not play a big role in the best medium blue. Logo must be present on the front side. As well as telephone, email, web and location. Big enough but not too big. Back can be redesigned Logo as well as name TozVar must be present. Important is the text: Van rental Disposal and clearing express transportation. Without bail in red should be noted somewhere. it should be modern but not too playful. rather serious but no beating company Thank you very much
Should not have
• Blue White and little red we want to change our existing design. Logo must remain the same as well as the color blue, whether dark or light Does not play a big role in the best medium blue. Logo must be present on the front side. As well as telephone, email, web and location. Big enough but not too big. Back can be redesigned Logo as well as name TozVar must be present. Important is the text: Van rental Disposal and clearing express transportation. Without bail in red should be noted somewhere. it should be modern but not too playful. rather serious but no beating company Thank you very much

```html
<!DOCTYPE html>
<html lang="en">
<head>
<meta charset="utf-8">
<title>TozVar GmbH – Business Cards</title>
<link rel="stylesheet" href="https://fonts.googleapis.com/css2?family=Open+Sans:wght@700;800&family=Roboto:wght@400;500&family=Roboto+Condensed:wght@400;700&display=swap">
<style>
  :root {
    --stage: #3b3b3d;
    --navy: #0f2a78;
    --navy-deep: #0a1f66;
    --steel: #7f97b3;
    --white: #ffffff;
    --ink: #111111;
    --red: #e3161f;
  }
  * { box-sizing: border-box; margin: 0; padding: 0; }
  html, body { width: 1200px; height: 1000px; overflow: hidden; }
  body { background: var(--stage); position: relative; font-family: "Roboto", Arial, sans-serif; }

  .card {
    position: absolute;
    width: 660px;
    height: 400px;
    border-radius: 24px;
    overflow: hidden;
    box-shadow: 0 18px 40px rgba(0,0,0,.45);
  }

  /* Back side */
  .card--back { left: 320px; top: 50px; background: var(--navy); }
  .back__mark {
    position: absolute; left: 70px; top: 78px;
    width: 100px; height: 100px; background: var(--white);
  }
  .back__name {
    position: absolute; left: 196px; top: 92px;
    font-family: "Open Sans", Arial, sans-serif; font-weight: 800;
    font-size: 68px; line-height: 1; letter-spacing: 1px; color: var(--white);
  }
  .back__legal {
    position: absolute; left: 592px; top: 110px;
    writing-mode: vertical-rl;
    font-family: "Roboto Condensed", Arial, sans-serif; font-size: 13px;
    letter-spacing: 1px; color: var(--white);
  }
  .back__rule {
    position: absolute; left: 48px; right: 48px; height: 1px; background: rgba(255,255,255,.8);
  }
  .back__rule--top { top: 200px; }
  .back__rule--bottom { top: 262px; }
  .services {
    position: absolute; left: 48px; right: 48px; top: 214px;
    display: flex; justify-content: space-between; align-items: center;
    font-family: "Roboto Condensed", Arial, sans-serif; font-size: 20px;
    letter-spacing: .5px; text-transform: uppercase; color: var(--white);
  }
  .services__dot { width: 6px; height: 6px; border-radius: 50%; background: var(--steel); }
  .back__band {
    position: absolute; left: 0; right: 0; top: 290px; height: 56px;
    background: var(--white);
  }
  .back__notice {
    position: absolute; left: 210px; top: 14px;
    font-family: "Roboto Condensed", Arial, sans-serif; font-weight: 700;
    font-size: 18px; color: var(--red); text-transform: uppercase;
  }

  /* Front side */
  .card--front { left: 220px; top: 530px; background: var(--white); }
  .front__mark {
    position: absolute; left: 62px; top: 70px;
    width: 190px; height: 190px; background: var(--navy-deep);
  }
  .front__name {
    position: absolute; right: 96px; top: 50px;
    font-family: "Open Sans", Arial, sans-serif; font-weight: 800;
    font-size: 60px; line-height: 1; letter-spacing: 1px; color: var(--navy-deep);
  }
  .front__legal {
    position: absolute; right: 68px; top: 66px;
    writing-mode: vertical-rl;
    font-family: "Roboto Condensed", Arial, sans-serif; font-size: 13px;
    letter-spacing: 1px; color: var(--navy-deep);
  }
  .contact {
    position: absolute; left: 320px; top: 200px; list-style: none;
    font-family: "Roboto", Arial, sans-serif; font-weight: 500;
    font-size: 24px; color: var(--ink);
  }
  .contact__item { display: flex; align-items: center; gap: 10px; height: 40px; }
  .contact__icon { width: 22px; height: 22px; flex: none; fill: var(--steel); }
</style>
</head>
<body>

<section class="card card--back" aria-label="Back of business card">
  <div class="back__mark"></div>
  <div class="back__name">TOZVAR</div>
  <div class="back__legal">GMBH</div>
  <div class="back__rule back__rule--top"></div>
  <div class="services">
    <span>Van Rental</span><span class="services__dot"></span>
    <span>Disposal and Clearing</span><span class="services__dot"></span>
    <span>Express Transportation</span>
  </div>
  <div class="back__rule back__rule--bottom"></div>
  <div class="back__band"><span class="back__notice">Without Bail</span></div>
</section>

<section class="card card--front" aria-label="Front of business card">
  <div class="front__mark"></div>
  <div class="front__name">TOZVAR</div>
  <div class="front__legal">GMBH</div>
  <ul class="contact">
    <li class="contact__item">
      <svg class="contact__icon" viewBox="0 0 24 24"><path d="M12 2a7 7 0 0 0-7 7c0 5 7 13 7 13s7-8 7-13a7 7 0 0 0-7-7zm0 9.5A2.5 2.5 0 1 1 12 6.5a2.5 2.5 0 0 1 0 5z"/></svg>
      <span>Werkstrasse 14, 8500 Frauenfeld</span>
    </li>
    <li class="contact__item">
      <svg class="contact__icon" viewBox="0 0 24 24"><path d="M6.6 10.8a15.1 15.1 0 0 0 6.6 6.6l2.2-2.2a1 1 0 0 1 1-.25 11.4 11.4 0 0 0 3.6.57 1 1 0 0 1 1 1V20a1 1 0 0 1-1 1A17 17 0 0 1 3 4a1 1 0 0 1 1-1h3.5a1 1 0 0 1 1 1c0 1.25.2 2.45.57 3.57a1 1 0 0 1-.25 1z"/></svg>
      <span>+41 70 123 45 67</span>
    </li>
    <li class="contact__item">
      <svg class="contact__icon" viewBox="0 0 24 24"><path d="M3 5h18a1 1 0 0 1 1 1v12a1 1 0 0 1-1 1H3a1 1 0 0 1-1-1V6a1 1 0 0 1 1-1zm9 8 8-5.5V7l-8 5.5L4 7v.5z"/></svg>
      <span>info@tozvar.ch</span>
    </li>
    <li class="contact__item">
      <svg class="contact__icon" viewBox="0 0 24 24"><path d="M12 2a10 10 0 1 0 0 20 10 10 0 0 0 0-20zm6.9 6h-3a15.7 15.7 0 0 0-1.4-3.6A8 8 0 0 1 18.9 8zM12 4a14 14 0 0 1 1.9 4h-3.8A14 14 0 0 1 12 4zM4.3 14a8 8 0 0 1 0-4h3.4a16.5 16.5 0 0 0 0 4zm.8 2h3a15.7 15.7 0 0 0 1.4 3.6A8 8 0 0 1 5.1 16zm3-8h-3a8 8 0 0 1 4.4-3.6A15.7 15.7 0 0 0 8.1 8zM12 20a14 14 0 0 1-1.9-4h3.8A14 14 0 0 1 12 20zm2.3-6H9.7a14.7 14.7 0 0 1 0-4h4.6a14.7 14.7 0 0 1 0 4zm.2 5.6a15.7 15.7 0 0 0 1.4-3.6h3a8 8 0 0 1-4.4 3.6zm1.8-5.6a16.5 16.5 0 0 0 0-4h3.4a8 8 0 0 1 0 4z"/></svg>
      <span>www.TozVar.ch</span>
    </li>
  </ul>
</section>

</body>
</html>
```